Lantern Hill Publicity is a new boutique Press Office with a small roster of well-chosen clients across an array of disciplines; from Art and Technology to Restaurants and Fashion. Based in Greenpoint Brooklyn, Lantern Hill Publicity achieves outstanding results through hard work, tenacity, efficiency and a sense of humor. We need a simple, versatile and classic design. We would like each side of the card to be white text on a black background.

Boutique

```html
<!DOCTYPE html>
<html lang="en">
<head>
<meta charset="utf-8">
<title>Lantern Hill Publicity – Business Card</title>
<link href="https://fonts.googleapis.com/css2?family=Open+Sans:wght@400;600&display=swap" rel="stylesheet">
<style>
  :root {
    --backdrop: #d9d9d9;
    --card: #121212;
    --ink: #ffffff;
    --ink-soft: #e6e6e6;
  }
  * { margin: 0; padding: 0; box-sizing: border-box; }
  html, body {
    width: 1200px; height: 900px; overflow: hidden;
    background: var(--backdrop);
    font-family: "Open Sans", Arial, sans-serif;
  }
  .stage { position: relative; width: 1200px; height: 900px; }
  .card {
    position: absolute;
    width: 640px; height: 366px;
    background: var(--card);
    color: var(--ink);
    box-shadow: 0 10px 28px rgba(0,0,0,0.28);
  }
  .card--back { left: 480px; top: 60px; }
  .card--front { left: 80px; top: 470px; }

  .wordmark {
    display: flex; align-items: center; gap: 14px;
    font-weight: 600; letter-spacing: 0.16em;
    text-transform: uppercase; color: var(--ink);
  }
  .wordmark__dot {
    width: 18px; height: 18px; border-radius: 50%;
    background: var(--ink); flex: none;
  }
  .card--back .wordmark {
    position: absolute; right: 48px; bottom: 120px; font-size: 24px;
  }
  .card--front .wordmark {
    position: absolute; left: 44px; top: 62px; font-size: 21px;
  }

  .contacts {
    position: absolute; left: 44px; top: 150px;
    list-style: none; font-size: 15px; line-height: 24px; color: var(--ink-soft);
  }
  .contacts li { display: flex; align-items: center; gap: 12px; }
  .contacts svg { width: 14px; height: 14px; flex: none; fill: var(--ink); }

  .holder {
    position: absolute; right: 44px; bottom: 40px; width: 300px;
    color: var(--ink);
  }
  .holder__name { font-size: 24px; font-weight: 400; }
  .holder__role { font-size: 15px; color: var(--ink-soft); margin-bottom: 26px; }
  .holder__address { font-size: 16px; line-height: 22px; font-style: normal; color: var(--ink-soft); }
</style>
</head>
<body>
<main class="stage">
  <section class="card card--back" aria-label="Card back">
    <div class="wordmark"><span class="wordmark__dot"></span>Lantern Hill Publicity</div>
  </section>

  <section class="card card--front" aria-label="Card front">
    <div class="wordmark"><span class="wordmark__dot"></span>Lantern Hill Publicity</div>

    <ul class="contacts">
      <li>
        <svg viewBox="0 0 16 16" aria-hidden="true"><path d="M4 1l2.5 3-1.5 2c1 2 3 4 5 5l2-1.5 3 2.5-1.5 2.5C8 14 2 8 1.5 3.5z"/></svg>
        917-555-0142
      </li>
      <li>
        <svg viewBox="0 0 16 16" aria-hidden="true"><path d="M4 0h8a1 1 0 0 1 1 1v14a1 1 0 0 1-1 1H4a1 1 0 0 1-1-1V1a1 1 0 0 1 1-1zm1 2v10h6V2zm3 11a1 1 0 1 0 0 2 1 1 0 0 0 0-2z"/></svg>
        917-555-0187
      </li>
      <li>
        <svg viewBox="0 0 16 16" aria-hidden="true"><path d="M1 3h14v10H1zm1.5 1.2L8 8.5l5.5-4.3z"/></svg>
        daniel@lanternhillpr.com
      </li>
      <li>
        <svg viewBox="0 0 16 16" aria-hidden="true"><circle cx="8" cy="8" r="7"/><path d="M1 8h14M8 1c-3 3-3 11 0 14M8 1c3 3 3 11 0 14" stroke="#121212" stroke-width="1" fill="none"/></svg>
        www.lanternhillpr.com
      </li>
    </ul>

    <div class="holder">
      <p class="holder__name">Daniel Marchetti</p>
      <p class="holder__role">Owner &amp; Founder</p>
      <address class="holder__address">LLC 418 Kent Lane Unit 2<br>Brooklyn, NY 11299</address>
    </div>
  </section>
</main>
</body>
</html>
```